I have a logo I just need a catchy bright flyer.
I offer a fine motor skills program using literacy and numeracy for children aged 4-6.

Tiny Steps Learning is a fun filled learning environment where children can develop their fine motor skills through exploring language, literacy & numeracy.
Special offer: Free trial. (conditions apply)

There is also a website www.tinystepslearning (Not live as yet)
email address tinystepslearning@quollnet.com
and phone 0491 305 724

Locations: Mount Waverley and Ashburton

```html
<!DOCTYPE html>
<html lang="en">
<head>
<meta charset="utf-8">
<title>Tiny Steps Learning – Fine Motor Skill Development</title>
<link rel="stylesheet" href="https://fonts.googleapis.com/css2?family=Arimo:wght@400;700&family=Archivo+Black&display=swap">
<style>
  :root {
    --page: #ffffff;
    --sky-top: #d6eef2;
    --sky-mid: #a9dcea;
    --sky-low: #7cc9e3;
    --navy: #1b2a4a;
    --text-grey: #2f3b4c;
    --grass-light: #86c057;
    --grass-mid: #66ad3d;
    --grass-deep: #4f952c;
    --offer-green: #d3df7a;
    --white: #ffffff;
    --band: #e8ad4c;
    --photo-a: #e9c7c9;
    --photo-b: #c7ae5a;
    --photo-c: #c98a7e;
    --logo-soft: #f3e2a6;
  }
  * { margin: 0; padding: 0; box-sizing: border-box; }
  html, body {
    width: 1000px; height: 1200px; overflow: hidden;
    background: var(--page);
  }
  .flyer {
    position: absolute; left: 37px; top: 0;
    width: 926px; height: 1200px; overflow: hidden;
    background: linear-gradient(180deg, var(--sky-top) 0%, var(--sky-mid) 45%, var(--sky-low) 75%);
    font-family: "Arimo", Arial, sans-serif;
    color: var(--navy);
    text-align: center;
  }
  .logo-art {
    position: absolute; left: 303px; top: 55px;
    width: 330px; height: 220px;
    border-radius: 50%;
    background: radial-gradient(ellipse at center, var(--logo-soft) 0%, rgba(243,226,166,0.5) 50%, rgba(243,226,166,0) 72%);
  }
  .brand-name {
    position: absolute; left: 0; right: 0; top: 278px;
    font-size: 70px; font-weight: 400; line-height: 80px;
    text-shadow: 0 0 14px rgba(255,255,255,0.9);
  }
  .tagline {
    position: absolute; left: 0; right: 0; top: 370px;
    font-size: 47px; font-weight: 400; line-height: 54px;
    text-shadow: 0 0 12px rgba(255,255,255,0.9);
  }
  .intro {
    position: absolute; left: 63px; width: 830px; top: 488px;
    text-align: left;
    font-size: 19px; line-height: 40px; letter-spacing: 1px;
    color: var(--text-grey);
    white-space: nowrap;
  }
  .intro strong { color: var(--navy); font-weight: 700; font-size: 21px; letter-spacing: 1.4px; }
  .photos { position: absolute; left: 42px; top: 594px; width: 854px; height: 172px; }
  .photo {
    position: absolute; top: 0; height: 172px;
    border: 4px solid var(--white);
    border-radius: 3px;
    box-shadow: 0 4px 10px rgba(0,0,0,0.3);
  }
  .photo-magnifier { left: 0; width: 266px; background: linear-gradient(135deg, #f2ece6, var(--photo-a)); }
  .photo-painting { left: 290px; width: 266px; background: linear-gradient(135deg, var(--photo-b), #8aa15a); }
  .photo-group { left: 576px; width: 278px; background: linear-gradient(135deg, var(--photo-c), #7fa9b8); }
  .website {
    position: absolute; left: 0; right: 0; top: 802px;
    font-size: 32px; font-weight: 700; letter-spacing: 3.6px;
  }
  .locations {
    position: absolute; left: 0; right: 0; top: 846px;
    font-size: 17px; font-weight: 700; letter-spacing: 1px;
    color: var(--navy);
  }
  .landscape {
    position: absolute; left: 0; top: 872px; width: 926px; height: 248px;
    background: linear-gradient(180deg, rgba(134,192,87,0) 0%, var(--grass-light) 14%, var(--grass-mid) 55%, var(--grass-deep) 100%);
  }
  .offer { position: absolute; left: 0; right: 0; top: 952px; color: var(--white); }
  .offer-label {
    font-family: "Archivo Black", "Arial Black", sans-serif;
    font-size: 38px; letter-spacing: 1px; line-height: 44px;
    text-shadow: 0 2px 4px rgba(0,0,0,0.35);
  }
  .offer-headline {
    font-family: "Archivo Black", "Arial Black", sans-serif;
    font-size: 54px; letter-spacing: 0.5px; line-height: 52px;
    color: var(--offer-green);
    text-shadow: 0 2px 4px rgba(0,0,0,0.35);
  }
  .offer-note {
    margin-top: 10px;
    font-size: 22px; font-weight: 700;
    text-shadow: 0 1px 3px rgba(0,0,0,0.35);
  }
  .contact-band {
    position: absolute; left: 0; bottom: 0; width: 926px; height: 80px;
    background: var(--band);
    color: var(--white);
    font-size: 32px; font-weight: 700; letter-spacing: 0.7px;
    text-shadow: 0 1px 3px rgba(0,0,0,0.3);
  }
  .contact-item { position: absolute; top: 19px; display: flex; align-items: center; gap: 12px; }
  .contact-email { left: 34px; }
  .contact-phone { left: 632px; gap: 6px; letter-spacing: 1.8px; }
</style>
</head>
<body>
<main class="flyer">
  <div class="logo-art" role="img" aria-label="Logo illustration area: smiling sun above three children on green grass"></div>
  <h1 class="brand-name">Tiny Steps Learning</h1>
  <h2 class="tagline">Fine Motor Skill Development</h2>
  <p class="intro"><strong>Tiny Steps Learning</strong> is a fun filled learning environment where children can<br>develop their fine motor skills through exploring language, literacy &amp; numeracy.</p>

  <div class="photos">
    <div class="photo photo-magnifier" role="img" aria-label="Photo: toddler looking through a magnifying glass at a table with coloured pencils"></div>
    <div class="photo photo-painting" role="img" aria-label="Photo: young girl painting on an easel"></div>
    <div class="photo photo-group" role="img" aria-label="Photo: group of smiling children looking down in a circle"></div>
  </div>

  <p class="website">www.tinystepslearning.com.au</p>
  <p class="locations">Mount Waverley &amp; Ashburton</p>

  <div class="landscape" role="img" aria-label="Illustration: green rolling hills with small trees"></div>

  <div class="offer">
    <p class="offer-label">SPECIAL OFFER:</p>
    <p class="offer-headline">FREE TRIAL</p>
    <p class="offer-note">(conditions apply)</p>
  </div>

  <footer class="contact-band">
    <div class="contact-item contact-email">
      <svg width="28" height="20" viewBox="0 0 28 20" aria-hidden="true">
        <rect x="1" y="1" width="26" height="18" fill="none" stroke="#fff" stroke-width="2.5"/>
        <path d="M1 1 L14 11 L27 1" fill="none" stroke="#fff" stroke-width="2.5"/>
      </svg>
      <span>tinystepslearning@quollnet.com</span>
    </div>
    <div class="contact-item contact-phone">
      <svg width="20" height="26" viewBox="0 0 20 26" aria-hidden="true">
        <path d="M5 2 L9 2 L10 8 L7 10 C8 14 10 17 13 19 L16 16 L19 19 L18 23 C10 24 2 14 3 4 Z" fill="#fff"/>
      </svg>
      <span>0491 305 724</span>
    </div>
  </footer>
</main>
</body>
</html>
```